website design for online company - registration of companies AUSTRALIA

website name: velmora482.com.au
purpose of the website: register NEW australian companies

once a client submits their order, our website will submit information to a government agency and in under 20 minutes, the client will receive their new company together with legal documentation:

key features:
- simplicity
- ease of use
- clarity
- fast
- competitive
- trust

our competitors:
www.quickdratel.com.au
www.zentrafirms.com.au

the website needs to be dynamic, clear and portray simplicity as the name suggests.

"register your company online with OREV in 3 simple steps"
1 fill in a short form
2 submit payment
3 receive your company

headings - similar to our competitors but needs to be different.

Design only no coding

if you have any questions, feel free to ask

people in business

Government

Serif

• simple
creative
elegant
• top graphics

```html
<!DOCTYPE html>
<html lang="en">
<head>
<meta charset="utf-8">
<title>Velmora482 – Register your company online</title>
<link rel="stylesheet" href="https://fonts.googleapis.com/css2?family=Source+Sans+3:ital,wght@0,400;0,600;0,700;1,700&display=swap">
<style>
:root{
  --blue:#3a8fd6;
  --blue-dark:#1a5a93;
  --blue-field:#175a91;
  --navy:#1d4f80;
  --ink:#333;
  --muted:#777;
  --grey-box:#e4e4e4;
  --rule:#d0d0d0;
  --white:#fff;
}
*{box-sizing:border-box;margin:0;padding:0}
html,body{width:746px;height:1200px;overflow:hidden}
body{position:relative;font-family:"Source Sans 3",Arial,sans-serif;color:var(--ink);background:var(--white)}
.abs{position:absolute}

.top{left:0;top:0;width:746px;height:445px;background:radial-gradient(ellipse at 50% 30%,#f8f8f8,#e6e6e6)}
.logo-box{left:84px;top:0;width:174px;height:118px;background:linear-gradient(#f4f4f4,#d9d9d9);border-radius:0 0 4px 4px;box-shadow:0 4px 6px rgba(0,0,0,.12);display:flex;flex-direction:column;align-items:center;justify-content:center;gap:10px}
.logo-mark{width:24px;height:24px;background:var(--blue);border-radius:3px}
.logo-name{font-size:21px;font-weight:700;color:var(--ink)}

.search{left:482px;top:22px;width:180px;height:24px;background:var(--white);border-radius:2px;font-size:8px;color:#bbb;padding:7px 8px;box-shadow:0 1px 2px rgba(0,0,0,.06)}
.search svg{position:absolute;right:5px;top:4px}

.nav{left:282px;top:69px;width:380px;height:48px;background:linear-gradient(#4aa0e2,#2f86d1);border-radius:3px;display:flex;align-items:center;justify-content:space-around;padding:0 6px;box-shadow:0 6px 8px -4px rgba(0,0,0,.25)}
.nav a{color:var(--white);font-size:7px;text-decoration:none;letter-spacing:-.1px}

.slider{left:84px;top:141px;width:578px;height:265px;background:linear-gradient(#f5f5f5,#dcdcdc);border-radius:6px;box-shadow:0 10px 10px -6px rgba(0,0,0,.3)}
.slide{left:90px;top:146px;width:566px;height:215px;background:var(--white)}
.slide h2{position:absolute;left:46px;top:68px;font-size:18px;font-weight:400;color:var(--ink)}
.slide p{position:absolute;left:46px;top:96px;width:140px;font-size:12px;line-height:16px;color:#999}
.slide-art{position:absolute;left:224px;top:14px;width:290px;height:196px;background:radial-gradient(ellipse at 55% 50%,#3b8fd3 0 12%,#c8cdd2 13% 45%,#fff 72%)}
.dots{left:332px;top:378px;display:flex;gap:5px}
.dots span{width:9px;height:9px;border-radius:50%;background:#cfcfcf;box-shadow:inset 0 1px 1px rgba(0,0,0,.15)}
.dots span.on{background:var(--blue)}

.tagline{left:0;top:464px;width:746px;text-align:center;font-size:16px;font-style:italic;font-weight:700;color:var(--ink)}
.step{top:509px;width:178px;height:104px;background:var(--grey-box);display:flex;flex-direction:column;align-items:center;padding-top:14px;gap:12px;font-size:13px;color:var(--ink)}
.step.active{background:var(--blue);color:var(--white)}
.step svg{height:46px}

.section-title{font-size:15px;font-weight:600;color:var(--ink)}
.welcome-rule{left:84px;top:685px;width:379px;height:1px;background:var(--rule)}
.welcome-photo{left:90px;top:709px;width:108px;height:102px;background:linear-gradient(135deg,#e8e8e8,#9aa0a6 55%,#4a4f55)}
.welcome-h{left:222px;top:700px;font-size:10px;font-weight:600}
.welcome-p{left:222px;top:720px;width:241px;font-size:8px;line-height:13px;color:var(--muted);text-align:justify}
.btn-more{left:222px;top:797px;width:51px;height:20px;background:var(--blue);color:var(--white);font-size:8px;border-radius:3px;display:flex;align-items:center;justify-content:center}

.why{left:482px;top:685px;width:180px;list-style:none;border-top:1px solid var(--rule)}
.why li{height:24px;border-bottom:1px solid var(--rule);font-size:8px;color:var(--muted);display:flex;align-items:center}

.band{left:0;top:868px;width:746px;height:265px;background:var(--blue);color:var(--white)}
.band-title{top:42px;font-size:13px;font-weight:400}
.testi{left:84px;display:flex;gap:12px;width:180px}
.testi-icon{flex:none;width:34px;height:34px;background:var(--blue-dark);display:flex;align-items:center;justify-content:center}
.testi-icon span{width:18px;height:18px;border:3px solid var(--white);border-radius:50%}
.testi p{font-size:8px;line-height:12px}
.contact-intro{left:282px;top:73px;width:180px;font-size:8px;line-height:10px}
.label{left:282px;font-size:8px}
.field{left:328px;width:135px;background:var(--blue-field);border-radius:3px}
.submit{left:328px;top:208px;width:48px;height:21px;background:linear-gradient(#fff,#ddd);color:var(--ink);font-size:8px;border-radius:3px;display:flex;align-items:center;justify-content:center}
.news{left:481px;width:181px;font-size:8px;line-height:12px;padding-bottom:8px;border-bottom:1px solid rgba(255,255,255,.25)}
.news .date{color:var(--navy);font-size:6px}

.footer{left:0;top:1133px;width:746px;height:67px;background:var(--navy);color:var(--white)}
.footer p{position:absolute;left:111px;top:28px;font-size:8px}
.social{position:absolute;left:570px;top:29px;display:flex;gap:6px}
.social span{width:16px;height:16px;border-radius:2px}
</style>
</head>
<body>

<div class="abs top"></div>

<div class="abs logo-box">
  <span class="logo-mark"></span>
  <span class="logo-name">Velmora482</span>
</div>

<div class="abs search">Search here ...
  <svg width="16" height="16" viewBox="0 0 16 16"><circle cx="6" cy="6" r="4.5" fill="none" stroke="#222" stroke-width="1.8"/><line x1="9.5" y1="9.5" x2="14.5" y2="14.5" stroke="#222" stroke-width="2.5" stroke-linecap="round"/></svg>
</div>

<nav class="abs nav">
  <a href="#">HOME</a><a href="#">ABOUT US</a><a href="#">HOW IT WORKS</a><a href="#">REGISTER COMPANY</a><a href="#">FAQ</a><a href="#">NEWS</a><a href="#">CONTACT</a>
</nav>

<div class="abs slider"></div>
<div class="abs slide">
  <h2>Consecte Facilisis</h2>
  <p>Nulla nec quam ut metus venenatis lacinia. metus venenatis lacinia.</p>
  <div class="slide-art" role="img" aria-label="Interlocking grey puzzle pieces with one blue piece at the centre"></div>
</div>
<div class="abs dots"><span class="on"></span><span></span><span></span><span></span></div>

<p class="abs tagline">"Register your company online with OREV in 3 simple steps"</p>

<div class="abs step active" style="left:84px">
  <svg viewBox="0 0 46 46" width="46"><rect x="6" y="4" width="28" height="36" fill="none" stroke="#fff" stroke-width="2"/><g stroke="#fff" stroke-width="1.5"><line x1="11" y1="13" x2="29" y2="13"/><line x1="11" y1="19" x2="29" y2="19"/><line x1="11" y1="25" x2="25" y2="25"/><line x1="11" y1="31" x2="22" y2="31"/></g><line x1="24" y1="30" x2="42" y2="12" stroke="#fff" stroke-width="3"/></svg>
  <span>Fill in a short form</span>
</div>
<div class="abs step" style="left:282px">
  <svg viewBox="0 0 46 46" width="46"><path d="M10 3h18l8 8v30H10z" fill="none" stroke="#3a8fd6" stroke-width="2"/><g stroke="#3a8fd6" stroke-width="1.5"><line x1="15" y1="18" x2="30" y2="18"/><line x1="15" y1="24" x2="27" y2="24"/><line x1="15" y1="30" x2="24" y2="30"/></g><circle cx="34" cy="35" r="8" fill="#3a8fd6"/><path d="M30 35l3 3 5-6" fill="none" stroke="#fff" stroke-width="2"/></svg>
  <span>Make Payment</span>
</div>
<div class="abs step" style="left:483px">
  <svg viewBox="0 0 60 46" width="60"><path d="M8 28l22-14 22 12-22 14z" fill="#3a8fd6"/><path d="M8 28v4l22 12 22-14v-4L30 40z" fill="#1d6fb5"/></svg>
  <span>Receive your company</span>
</div>

<h3 class="abs section-title" style="left:84px;top:650px">Welcome to Velmora482</h3>
<div class="abs welcome-rule"></div>
<div class="abs welcome-photo" role="img" aria-label="Hand resting on a computer mouse on a mouse pad"></div>
<p class="abs welcome-h">Nunc euismod malesuada sapien</p>
<p class="abs welcome-p">Viraulputate enim luctus in. Suspendisse est purus, mollis dictum posuere et, pharetra aliquet arcu. Sed interdum luctus ante, ornare tempus tortor facilisis vel. Suspendisse consequat placerat varius. Suspendisse potenti. tempus tortor facilisis vel. Suspendisse consequat placerat varius. Suspendisse potenti.</p>
<div class="abs btn-more">More Info</div>

<h3 class="abs section-title" style="left:482px;top:650px">Why Use Us</h3>
<ul class="abs why">
  <li>Nullam imperdiet tristique dolor, sed pretium</li>
  <li>Suspendisse nec ante quis metus aliquet</li>
  <li>Maecenas vitae tortor eu ligula sollic ibot un</li>
  <li>Sed cursus elit laoreet lectus eleifend soda</li>
  <li>Duis gravida vulputate orci, sit amet euism</li>
  <li>Proin semper ipsum et magna interdum temp</li>
</ul>

<section class="abs band">
  <h3 class="abs band-title" style="left:84px">Testimonials</h3>
  <div class="abs testi" style="top:70px"><div class="testi-icon"><span></span></div><p>Pellentesque rutrum turpis vel eros elementum consectetur suscipit orci egestas. + more</p></div>
  <div class="abs testi" style="top:128px"><div class="testi-icon"><span></span></div><p>Vivamus aliquet massa ut risus uno euismod eget interdum risus ires vehicula magni. + more</p></div>
  <div class="abs testi" style="top:186px"><div class="testi-icon"><span></span></div><p>Lorem ipsum dolor sit amet, consec tetur adipisicing elit indidunt labor aspen dolores. + more</p></div>

  <h3 class="abs band-title" style="left:282px">Quick Contact</h3>
  <p class="abs contact-intro">Kindly drop your contact details and comments on our services for us to</p>
  <span class="abs label" style="top:105px">Name :</span><div class="abs field" style="top:102px;height:17px"></div>
  <span class="abs label" style="top:130px">Email :</span><div class="abs field" style="top:126px;height:18px"></div>
  <span class="abs label" style="top:155px">Message:</span><div class="abs field" style="top:151px;height:48px"></div>
  <div class="abs submit">SUBMIT</div>

  <h3 class="abs band-title" style="left:481px">Latest News</h3>
  <p class="abs news" style="top:68px"><span class="date">10 / 02 / 2014</span> - Ornare cursus mi, sit amet consectetur ligula egestas vitae.</p>
  <p class="abs news" style="top:110px"><span class="date">09 / 04 / 2014</span> - Curabitur vehicula condimentum purus, nec suscipit metus consequat nec.</p>
  <p class="abs news" style="top:151px"><span class="date">08 / 05 / 2014</span> - Vestibulum luctus consequat odio, blandit consectetur purus posu.</p>
  <p class="abs news" style="top:193px;border:0"><span class="date">07 / 03 / 2014</span> - Nam aliquet lorem quis nisl porta dictum consectetur mauris molestie.</p>
</section>

<footer class="abs footer">
  <p>Copy rights(c) 2014 velmora482 | All rights reserved.</p>
  <div class="social">
    <span style="background:#3b5b99"></span><span style="background:#4cb6d8"></span><span style="background:#e8861e"></span><span style="background:#d94a3a"></span>
  </div>
</footer>

</body>
</html>
```